WordPress website design for wealth management company

A modern clean look website for a service company. This is mostly for information only, with a form to capture prospect contact information and schedule a 15 minutes call. There will be several static pages describe what services we offer, how we are different, and a blog section for posting articles and share resources. A section for client testimonials.
I want a website that is easy to understand and maintain. No proprietary plugins that cost extra. The main thing I need help is the visual layout / color palette that present a clean and professional look, select the suitable stock photos that convey the image of trust, professional, innovative, and high service.
Some websites with style I like include the following
- https://www.halbrookwealth.com/
- https://www.morvatefinancialorbits.com/
- https://tamblinfunds.com/private-equity-partners/
Also some websites in other industries with clean modern look
- https://plorvix.com/
- https://gravola.com/
- https://www.brisotelka.com/
I want the end product to be a fully functional website that I can upload into web hosting service I use and I can easily add content and maintain myself in the future.

```html
<!DOCTYPE html>
<html lang="en">
<head>
<meta charset="utf-8">
<title>Ardenne Wealth — Website Design</title>
<link href="https://fonts.googleapis.com/css2?family=Manrope:wght@400;500;600;700&family=Nunito+Sans:wght@300;400;600&display=swap" rel="stylesheet">
<style>
:root{
  --gold:#fcba28;
  --plum:#431b6a;
  --purple:#50227e;
  --mist:#f5f2f7;
  --lavender:#efecf4;
  --board:#ebebeb;
  --ink:#2b2b33;
  --muted:#6c6a75;
  --line:#e2dfe8;
  --white:#ffffff;
}
*{margin:0;padding:0;box-sizing:border-box}
html,body{width:1200px;height:2884px;overflow:hidden;background:var(--board)}
body{position:relative;font-family:"Nunito Sans",sans-serif;color:var(--ink)}
.head{font-family:"Manrope",sans-serif}
.abs{position:absolute}

/* brand board */
.brand-mark{left:201px;top:132px;display:flex;align-items:center;gap:12px}
.brand-dot{width:30px;height:30px;border-radius:50%;border:3px solid var(--purple)}
.brand-name{font-family:"Manrope",sans-serif;font-weight:700;font-size:23px;letter-spacing:2px;color:var(--purple);line-height:1.05}
.board-label{font-family:"Manrope",sans-serif;font-size:25px;color:#333;font-weight:400}
.font-list{left:570px;top:148px;font-family:"Manrope",sans-serif;font-size:16px;color:#555;line-height:25px}
.swatches{left:838px;top:138px;display:flex;gap:11px}
.swatch{width:41px;text-align:center;font-size:9.5px;color:#555}
.swatch span{display:block;width:41px;height:41px;border-radius:50%;margin-bottom:7px}

/* site */
.site{left:222px;top:279px;width:792px;height:2498px;background:var(--white);overflow:hidden}
.nav{height:44px;position:relative;display:flex;align-items:center;padding:0 57px}
.logo{display:flex;align-items:center;gap:6px}
.logo-dot{width:15px;height:15px;border-radius:50%;border:2px solid var(--purple)}
.logo-name{font-family:"Manrope",sans-serif;font-weight:700;font-size:11px;letter-spacing:1px;color:var(--purple);line-height:1}
.nav-links{margin-left:auto;display:flex;align-items:center;gap:20px;font-size:8px;color:#444}
.nav-cta{border:1px solid var(--gold);padding:8px 14px;color:var(--plum);font-weight:600;font-family:"Manrope",sans-serif}
.photo{background:linear-gradient(135deg,#e9e6e2,#cfc9c7)}

.hero{height:396px;position:relative}
.hero-photo{left:0;top:0;width:396px;height:396px;background:linear-gradient(160deg,#eeeeec 0%,#d8d6d4 45%,#6a3a92 70%,#4a2a6a 100%)}
.hero-panel{left:396px;top:0;width:396px;height:396px;background:linear-gradient(135deg,var(--purple),var(--plum))}
.eyebrow{font-size:7.5px;letter-spacing:3px;color:#d8cde6;text-transform:uppercase}
.hero h1{font-family:"Manrope",sans-serif;font-weight:600;font-size:40px;line-height:41px;color:var(--white)}
.hero h1 em{font-style:normal;color:var(--gold)}
.checks{display:flex;gap:36px;font-size:8px;color:#e8e0f0}
.checks div{display:flex;align-items:center;gap:5px}
.btn-outline{display:inline-block;border:1px solid var(--gold);font-family:"Manrope",sans-serif;font-weight:600;font-size:7.5px;color:var(--white);text-align:center}

.stats{height:157px;background:var(--lavender);position:relative}
.stat{top:50px;transform:translateX(-50%);text-align:center}
.stat b{display:block;font-family:"Manrope",sans-serif;font-weight:500;font-size:36px;color:var(--plum);line-height:38px}
.stat small{font-size:8px;color:var(--muted)}
.divider{top:58px;width:1px;height:42px;background:#d6d1de}

.services{height:329px;position:relative;text-align:center}
.section-title{font-family:"Manrope",sans-serif;font-weight:500;color:var(--plum)}
.services .section-title{padding-top:53px;font-size:25px;line-height:27px}
.lede{font-size:9px;color:#555;line-height:13px}
.cards{position:absolute;left:57px;top:173px;display:flex;gap:16px}
.card{width:100px;height:98px;border:1px solid var(--line);display:flex;flex-direction:column;align-items:center;justify-content:center;gap:6px;font-size:7.5px;color:#555;line-height:9.5px}

.different{height:408px;position:relative}
.diff-intro{left:0;top:0;width:396px;height:212px;background:var(--lavender);padding:44px 29px}
.diff-intro h2{font-size:24px;font-weight:500;margin-bottom:14px}
.diff-intro p{font-size:9px;line-height:14px;color:#444}
.link{display:inline-block;margin-top:16px;font-size:7.5px;color:var(--plum);border-bottom:1px solid var(--gold);padding-bottom:2px}
.diff-engage{left:0;top:212px;width:199px;height:196px;background:var(--purple);padding:38px 31px;color:var(--white)}
.diff-engage p{font-family:"Manrope",sans-serif;font-size:12px;line-height:16.5px}
.couple-photo{left:199px;top:212px;width:197px;height:196px;background:linear-gradient(135deg,#efe9e2,#d9c07a 55%,#7a4aa0)}
.stairs-photo{left:396px;top:0;width:396px;height:408px;background:linear-gradient(160deg,#e4e4e4,#bdbdbd 55%,#8c7d6e)}
.video-box{left:594px;top:212px;width:198px;height:196px;background:var(--gold);padding:32px 30px}
.video-box .kicker{font-size:7.5px;letter-spacing:2px;color:var(--plum);line-height:12px}
.play{display:flex;align-items:center;gap:8px;margin-top:53px;font-size:7.5px;color:var(--plum)}

.testimonial{height:247px;position:relative}
.testimonial h2{font-size:25px;line-height:27px;font-weight:500;color:var(--plum)}
.quote-rule{left:296px;top:58px;width:1px;height:154px;background:var(--line)}
.quote{left:313px;top:54px;width:270px;font-size:8.8px;line-height:15px;color:#444}
.author{font-size:8px;color:var(--plum)}
.arrow{width:26px;height:26px;border-radius:50%;border:1px solid #bbb;display:flex;align-items:center;justify-content:center}
.hr{left:57px;bottom:0;width:678px;height:1px;background:var(--line)}

.news{height:415px;position:relative}
.news .section-title{position:absolute;top:50px;width:100%;text-align:center;font-size:24px}
.news-card{top:105px;width:205px}
.news-img{width:205px;height:204px}
.news-card h3{font-family:"Manrope",sans-serif;font-weight:500;font-size:12px;line-height:15.5px;color:#222;margin-top:22px}
.news-card .more,.list-item .more{font-size:7px;color:var(--plum);margin-top:12px;display:block}
.news-rule{left:284px;top:105px;width:1px;height:275px;background:var(--line)}
.list-item{left:528px;width:208px;border-bottom:1px solid var(--line);padding-bottom:16px}
.list-item h4{font-family:"Manrope",sans-serif;font-weight:500;font-size:9.5px;line-height:14px;color:#222}

.cta{height:235px;background:linear-gradient(135deg,var(--purple),var(--plum));text-align:center;color:var(--white);padding-top:54px}
.cta h2{font-size:24px;font-weight:600}
.cta h2 em{font-style:normal;color:var(--gold)}
.cta p{font-size:9px;line-height:13px;color:#ddd1ea;margin-top:14px}
.cta .btn-outline{margin-top:18px;width:111px;height:25px;line-height:23px}

.footer{height:267px;background:var(--mist);position:relative}
.social{top:64px;width:16px;height:16px;border-radius:50%;background:var(--gold)}
.col{top:100px;font-size:7px;color:#555;line-height:14.5px}
.col h5{font-family:"Manrope",sans-serif;font-weight:500;font-size:8.5px;color:var(--plum);margin-bottom:6px}
.legal{top:204px;font-size:6.5px;color:#888}
</style>
</head>
<body>

<!-- brand board -->
<div class="abs brand-mark">
  <div class="brand-dot"></div>
  <div class="brand-name">ARDENNE<br>WEALTH</div>
</div>
<div class="abs board-label" style="left:570px;top:100px">Fonts:</div>
<div class="abs font-list">Manrope<br>Nunito Sans</div>
<div class="abs board-label" style="left:838px;top:100px">Colors:</div>
<div class="abs swatches">
  <div class="swatch"><span style="background:#fcba28"></span>#fcba28</div>
  <div class="swatch"><span style="background:#431b6a"></span>#431b6a</div>
  <div class="swatch"><span style="background:#50227e"></span>#50227e</div>
  <div class="swatch"><span style="background:#f5f2f7;box-shadow:0 0 0 1px #ddd inset"></span>#f5f2f7</div>
</div>

<!-- website -->
<main class="abs site">
  <header class="nav">
    <div class="logo"><div class="logo-dot"></div><div class="logo-name">ARDENNE<br>WEALTH</div></div>
    <nav class="nav-links">
      <span>About</span><span>Services</span><span>News &amp; Insights</span><span>Contact</span>
      <span class="nav-cta">Schedule 15 Minute Call</span>
      <svg width="10" height="10" viewBox="0 0 10 10"><circle cx="4.2" cy="4.2" r="3.2" fill="none" stroke="#50227e" stroke-width="1"/><path d="M6.6 6.6 9 9" stroke="#50227e"/></svg>
    </nav>
  </header>

  <section class="hero">
    <div class="abs hero-photo" role="img" aria-label="Photo of a smiling man in a purple sweater holding a coffee mug and phone in a bright office"></div>
    <div class="abs hero-panel">
      <div class="abs eyebrow" style="left:58px;top:147px">Plan happily with us</div>
      <h1 class="abs" style="left:58px;top:160px">Find <em>Calmness</em><br>in Managing<br>Your Wealth</h1>
      <div class="abs checks" style="left:58px;top:299px">
        <div><svg width="9" height="9" viewBox="0 0 9 9"><circle cx="4.5" cy="4.5" r="3.8" fill="none" stroke="#fcba28"/><path d="M2.7 4.6 4 5.8 6.3 3.3" fill="none" stroke="#fcba28"/></svg>Customer Oriented Aproach</div>
        <div><svg width="9" height="9" viewBox="0 0 9 9"><circle cx="4.5" cy="4.5" r="3.8" fill="none" stroke="#fcba28"/><path d="M2.7 4.6 4 5.8 6.3 3.3" fill="none" stroke="#fcba28"/></svg>Professional Services</div>
      </div>
      <span class="abs btn-outline" style="left:60px;top:331px;width:112px;height:29px;line-height:27px">See How We Can Help</span>
    </div>
  </section>

  <section class="stats">
    <div class="abs stat" style="left:88px"><b>175</b><small>Fortune Sponsors</small></div>
    <div class="abs divider" style="left:183px"></div>
    <div class="abs stat" style="left:314px"><b>36%</b><small>Clients &amp; Families/Employee Owned</small></div>
    <div class="abs divider" style="left:443px"></div>
    <div class="abs stat" style="left:536px"><b>43</b><small>Team Members</small></div>
    <div class="abs divider" style="left:628px"></div>
    <div class="abs stat" style="left:714px"><b>28</b><small>Offices</small></div>
  </section>

  <section class="services">
    <h2 class="section-title">We Provide Comprehensive<br>Wealth Management Solutions</h2>
    <p class="lede" style="margin-top:24px">Our team of experts works closely with you to create a customized<br>plan that aligns with your unique needs and aspirations</p>
    <div class="cards">
      <div class="card"><svg width="20" height="22" viewBox="0 0 20 22" fill="none" stroke="#50227e"><circle cx="10" cy="7" r="5.5"/><path d="M10 12.5V21M6 17c2 0 4 1 4 1s2-1 4-1"/></svg>Investment<br>Management</div>
      <div class="card"><svg width="20" height="22" viewBox="0 0 20 22" fill="none" stroke="#50227e"><rect x="3" y="2" width="11" height="17"/><path d="M6 7h5M6 10h5M6 13h3"/><rect x="12" y="11" width="5" height="8"/></svg>Financial<br>Planning</div>
      <div class="card"><svg width="20" height="22" viewBox="0 0 20 22" fill="none" stroke="#50227e"><circle cx="10" cy="5" r="3"/><path d="M4 20v-5c0-3 3-5 6-5s6 2 6 5v5M2 20h16"/></svg>Retirement<br>Planning</div>
      <div class="card"><svg width="20" height="22" viewBox="0 0 20 22" fill="none" stroke="#50227e"><rect x="3" y="3" width="14" height="16"/><path d="M6 8h8M6 11h8M6 14h5"/></svg>Tax<br>Planning</div>
      <div class="card"><svg width="20" height="22" viewBox="0 0 20 22" fill="none" stroke="#50227e"><path d="M2 11 10 3l8 8M4 9v11h12V9"/><rect x="8" y="13" width="4" height="7"/></svg>Estate<br>Planning</div>
      <div class="card"><svg width="20" height="22" viewBox="0 0 20 22" fill="none" stroke="#50227e"><path d="M10 2 17 5v6c0 5-3 8-7 9-4-1-7-4-7-9V5z"/><path d="M10 8v6M7 11h6"/></svg>Insurance<br>Planning</div>
    </div>
  </section>

  <section class="different">
    <div class="abs diff-intro">
      <h2 class="section-title">How We Are Different?</h2>
      <p>Our strategic approach entails a thorough assessment of how Ardenne Wealth can assist you in achieving financial independence, thereby optimizing your financial well-being</p>
      <span class="link">Discover More</span>
    </div>
    <div class="abs stairs-photo" role="img" aria-label="Aerial photo of three colleagues sitting on stone steps with a laptop"></div>
    <div class="abs diff-engage">
      <p>Let's engage in a substantive discussion regarding your financial prospects and future</p>
      <span class="btn-outline" style="margin-top:28px;width:111px;height:26px;line-height:24px">Schedule 15 Minute Call</span>
    </div>
    <div class="abs couple-photo" role="img" aria-label="Photo of a senior couple reviewing documents together"></div>
    <div class="abs video-box">
      <div class="kicker">EXPLORING WEALTH<br>MANAGEMENT: SEE MOST<br>RECENT VIDEO RESOURCE</div>
      <div class="play"><svg width="27" height="27" viewBox="0 0 27 27"><circle cx="13.5" cy="13.5" r="12.5" fill="none" stroke="#50227e"/><path d="M10.5 8.5v10l8-5z" fill="#50227e"/></svg>Play Video</div>
    </div>
  </section>

  <section class="testimonial">
    <svg class="abs" style="left:57px;top:58px" width="26" height="18" viewBox="0 0 26 18"><path d="M1 0h10v9l-5 9H2l4-8H1zM15 0h10v9l-5 9h-4l4-8h-5z" fill="#fcba28"/></svg>
    <h2 class="abs head" style="left:57px;top:90px">Don't Take<br>Our Word,<br>Take Theirs</h2>
    <div class="abs quote-rule"></div>
    <div class="abs quote">
      <p>"I have been a client of Ardenne Wealth for several years now, and I couldn't be happier with their services. As someone who has always been cautious about my financial future, finding a trustworthy wealth management company was a top priority for me, and Ardenne Wealth has exceeded my expectations in every way. They don't just offer cookie-cutter solutions; instead, they tailor their strategies to my individual needs and circumstances."</p>
      <p class="author" style="margin-top:12px">Lucas Fennimore</p>
      <p style="font-size:6.5px;color:#888">CEO and Owner</p>
    </div>
    <div class="abs arrow" style="left:710px;top:62px"><svg width="10" height="8" viewBox="0 0 10 8"><path d="M9 4H1M4 1 1 4l3 3" fill="none" stroke="#aaa"/></svg></div>
    <div class="abs arrow" style="left:710px;top:94px;border-color:#50227e"><svg width="10" height="8" viewBox="0 0 10 8"><path d="M1 4h8M6 1l3 3-3 3" fill="none" stroke="#50227e"/></svg></div>
    <div class="abs hr"></div>
  </section>

  <section class="news">
    <h2 class="section-title">News and Resources</h2>
    <article class="abs news-card" style="left:59px">
      <div class="news-img photo" role="img" aria-label="Photo of a man on the phone leaning against a bookshelf by tall windows"></div>
      <h3>Critical Importance of Immediate Tax Planning</h3>
      <span class="more">Read Full Story</span>
    </article>
    <div class="abs news-rule"></div>
    <article class="abs news-card" style="left:304px">
      <div class="news-img" style="background:linear-gradient(135deg,#dcdcdc,#f2b94a 55%,#3a3a3a)" role="img" aria-label="Photo of a woman in glasses reading a notebook"></div>
      <h3>The Big 12: Retirement Planning Questions for a Stress-Free Future</h3>
      <span class="more">Read Full Story</span>
    </article>
    <div class="abs list-item" style="top:110px"><h4>The Human Touch in Finance: Why Personalized Advice Matters</h4><span class="more">Explore Case Study</span></div>
    <div class="abs list-item" style="top:197px"><h4>Beyond Stocks and Bonds: Here We Discuss About Alternative Investment in Wealth Management and Financial Market</h4><span class="more">Explore Case Study</span></div>
    <div class="abs list-item" style="top:300px"><h4>Charitable Giving with Impact: Exploring Effective Philanthropy Strategies to Maximize Social and Environmental Change</h4><span class="more">Explore Case Study</span></div>
  </section>

  <section class="cta">
    <h2 class="head">Here to <em>Support</em> Your Journey</h2>
    <p>From the moment you set out on your career path to the time<br>you're considering retirement, we're here to provide guidance</p>
    <span class="btn-outline">Schedule 15 Minute Call</span>
  </section>

  <footer class="footer">
    <div class="abs logo" style="left:57px;top:56px"><div class="logo-dot"></div><div class="logo-name">ARDENNE<br>WEALTH</div></div>
    <div class="abs social" style="left:697px"></div>
    <div class="abs social" style="left:719px"></div>
    <div class="abs col" style="left:57px"><h5>Company</h5>About<br>How We Help<br>Careers<br>Contact</div>
    <div class="abs col" style="left:205px"><h5>Services</h5>Investment Mangement<br>Financial Planning<br>Retirement Planning</div>
    <div class="abs col" style="left:382px"><h5>Quick Links</h5>Services<br>FAQs<br>Offices</div>
    <div class="abs col" style="left:526px"><h5>Press</h5>Blog Articles<br>Resources</div>
    <div class="abs col" style="left:680px"><h5>Contact Us</h5>info@ardennewealth.com<br>+1 234 555 0190</div>
    <div class="abs legal" style="left:57px">© 2023 - Ardenne Wealth</div>
    <div class="abs legal" style="right:57px">Privacy Policy | Terms of Use | Cookie Policy</div>
  </footer>
</main>

</body>
</html>
```